Book cover for a sci fi book called The Velvet Assembly

Dear Pixel Harbor team,

I would need a book cover design for my sci fi book, 'The Velvet Assembly'.

I will start by briefing you about the book's content, then I would like to advice you about a few possible book cover scenarios that I could imagine having for the book, and on which I would like to ask you to work on.

Book abstract:

The velvet assembly is a technically developed and spiritually evolved society from a distant galaxy.

Main location the actions take place: Planet Earth, globalized world, former Northern Germany, a new isolated high tech city at the sea, called Lees, inhabitants from everywhere, one government, one religion.
• Year: 2093
• The Velvet Assembly: solar system with 7 suns. The inhabitans of the velvet assembly have no physical body, only energetical bodies. Only when visiting Earth, they can incarnate at will.

The action starts on planet Earth, where a group of 4 people, two women and two males, who meet through different circumstances and decide to follow together a spiritual and philiosophical path towards self development and evolution. They meet an incarnated master from the velvet assembly who leads their path. At the end of the books, they reach a form of enlightment and transcende to The Velvet Assembly, they only come to know at the end the truth about the real origin of their master.

For the book cover, no matter what ideas you choose, please use max three predominant colors for that, red, yellow and orange. The book cover should inspire warmth.

Suggestions for the design:
- an abstract sun
- a cosmic view of the velvet assembly
- an abstractized design of a sacred geometry shape
- sun in the upper left corner, shining with visible rays on the whole surface of the book cover, a group of 4 people with the female old master sitting by their side in the lower right corner
- an out of the box Ufo, please choose for example an asymmetrical shape, definately not the usual flying sorcer, departing from the velvet assembly solar system, cosmic view from above
- PLEASE FEEL FREE TO BRAINSTROM ON YOUR OWN IDEAS BASED ON WHAT THE BOOK ABSTRACT INSPIRED YOU

For any questions, I am atbyour disposal.

I am looking forward to your design, thank you in advance for that.

Kind regards,
Mira

Target Market(s)

Sci Fi enthusiasts
Philosophers

Font styles to use
Serif

Colors
fbee3e
ffc214
faa54b
f37122
f04a50

Requirements
Must have
• For the book cover, no matter what ideas you choose, please use max three predominant colors for that, red, yellow and orange and/or any derived hues. The book cover should inspire warmth.
• Suggestions for the design:
• - an abstract sun
• - a cosmic view of the velvet assembly
• - an abstractized design of a sacred geometry shape
• - sun in the upper left corner, shining with visible rays on the whole surface of the book cover, a group of 4 people with the female old master sitting by their side in the lower right corner
• - an out of the box Ufo, please choose for example an asymmetrical shape, definately not the usual flying sorcer, departing from the velvet assembly solar system, cosmic view from above
• - PLEASE FEEL FREE TO BRAINSTROM ON YOUR OWN IDEAS BASED ON WHAT THE BOOK ABSTRACT INSPIRED YOU
Nice to have
• Minimalistic and modern design
Should not have
• dark or grey shades
• phtographs

```html
<!DOCTYPE html>
<html lang="en">
<head>
<meta charset="utf-8">
<title>The Velvet Assembly — Book Cover</title>
<link href="https://fonts.googleapis.com/css2?family=Poiret+One&display=swap" rel="stylesheet">
<style>
  :root {
    --sun-white: #fff6d6;
    --sun-yellow: #fbee3e;
    --sun-gold: #ffc214;
    --sun-orange: #faa54b;
    --sun-deep: #f37122;
    --sun-red: #f04a50;
    --ember: #c9321f;
    --ink: #262626;
    --ink-edge: #8a8a8a;
    --page: #f2f2f2;
  }
  html, body {
    margin: 0;
    padding: 0;
    width: 927px;
    height: 1200px;
    overflow: hidden;
    background: var(--page);
  }
  .cover {
    position: relative;
    width: 927px;
    height: 1200px;
    overflow: hidden;
  }
  .cover__art {
    position: absolute;
    inset: 0;
    background:
      radial-gradient(ellipse 22% 16% at 28% 78%, var(--sun-deep) 0%, rgba(243,113,34,0) 100%),
      radial-gradient(ellipse 35% 25% at 60% 70%, var(--sun-white) 0%, rgba(255,246,214,0) 100%),
      radial-gradient(ellipse 40% 30% at 35% 50%, var(--sun-gold) 0%, rgba(255,194,20,0) 100%),
      radial-gradient(ellipse 60% 40% at 50% 25%, var(--sun-orange) 0%, rgba(250,165,75,0) 100%),
      linear-gradient(180deg, var(--ember) 0%, var(--sun-deep) 22%, var(--sun-orange) 45%, var(--sun-gold) 65%, var(--sun-orange) 85%, var(--sun-deep) 100%);
  }
  .cover__title {
    position: absolute;
    left: 0;
    top: 0;
    width: 927px;
    height: 1200px;
  }
  .title-word,
  .title-article,
  .author-name {
    font-family: "Poiret One", sans-serif;
    fill: var(--ink);
    stroke: var(--ink-edge);
    stroke-width: 1.2;
    paint-order: stroke fill;
  }
  .title-word {
    font-size: 150px;
    stroke-width: 2;
  }
  .title-article {
    font-size: 58px;
  }
  .author-name {
    font-size: 58px;
  }
</style>
</head>
<body>
  <main class="cover">
    <div class="cover__art" role="img" aria-label="Abstract close-up of a blazing sun surface with fiery orange, red and yellow crystalline bursts"></div>
    <svg class="cover__title" viewBox="0 0 927 1200" xmlns="http://www.w3.org/2000/svg" aria-label="The Velvet Assembly by Author's Name">
      <text class="title-article" x="70" y="425">the</text>
      <text class="title-word" x="62" y="570" textLength="802" lengthAdjust="spacingAndGlyphs">VELVET</text>
      <text class="title-word" x="62" y="705" textLength="802" lengthAdjust="spacingAndGlyphs">ASSEMBLY</text>
      <text class="author-name" x="463" y="1145" text-anchor="middle" textLength="560" lengthAdjust="spacingAndGlyphs">AUTHOR’S NAME</text>
    </svg>
  </main>
</body>
</html>
```